Retail Jewelry Business Card Design Project

We are in need of a new business card design for a retail jewelry store. This store is in the business of fine jewelry including but not specific to bridal jewelry, diamonds, designer jewelry and watches.

This store has been in business for 20 years but continues to strive for a modern professional appeal. The main colors use for this business are a royal blue, white and silver.

Target Market(s)

Target market is ages 18-50

Industry/Entity Type

Jewelry

Requirements
Must have
• Sales Person Name
Sales Person Email Address

Store Address
Store Phone
Website

Standard business card size. No odd shapes or sizes.
Nice to have
• Overall modern feel for card.

We have thought that a design with a nice feature of the logo on the back of the card would be nice but open to ideas.
Should not have
• No specific images of jewelry should be used.

```html
<!DOCTYPE html>
<html lang="en">
<head>
<meta charset="utf-8">
<title>Marlow Reed – Business Card</title>
<link href="https://fonts.googleapis.com/css2?family=Open+Sans:wght@400;600;700&display=swap" rel="stylesheet">
<style>
  :root {
    --page-bg: #eceef2;
    --royal-center: #3f56a6;
    --royal-mid: #2f4290;
    --royal-edge: #232f6e;
    --silver-light: #f4f5f7;
    --silver-mid: #b9bcc3;
    --silver-dark: #6f737b;
    --ink-white: #ffffff;
  }
  * { box-sizing: border-box; margin: 0; padding: 0; }
  html, body {
    width: 1200px; height: 1000px; overflow: hidden;
    background: var(--page-bg);
    font-family: "Open Sans", Arial, sans-serif;
  }
  .sheet {
    position: relative; width: 1200px; height: 1000px;
    display: flex; align-items: center; justify-content: center; gap: 34px;
  }
  .card {
    position: relative; width: 540px; height: 306px;
    border-radius: 10px; overflow: hidden;
    background: radial-gradient(ellipse 60% 75% at 45% 42%, var(--royal-center) 0%, var(--royal-mid) 55%, var(--royal-edge) 100%);
    box-shadow: 0 6px 14px rgba(0,0,0,0.28);
    color: var(--ink-white);
  }
  .silver-edge {
    position: absolute; top: 0; bottom: 0; width: 14px;
    background: linear-gradient(90deg, var(--silver-dark), var(--silver-light) 45%, var(--silver-mid) 70%, var(--silver-dark));
  }
  .card--front .silver-edge { left: 0; }
  .card--back .silver-edge { right: 0; }
  .brand-name {
    font-weight: 600; font-size: 30px; letter-spacing: 0.5px;
    color: var(--ink-white); white-space: nowrap;
  }
  .card--front .brand-name { position: absolute; top: 26px; right: 30px; }
  .card--back .brand-name {
    position: absolute; top: 50%; left: 50%; transform: translate(-50%, -50%);
    font-size: 34px;
  }
  .contact-list {
    position: absolute; left: 28px; bottom: 22px; list-style: none;
    font-size: 12.5px; line-height: 18px;
  }
  .contact-list li { display: flex; align-items: flex-start; gap: 8px; }
  .contact-list svg { width: 15px; height: 15px; margin-top: 1.5px; flex: none; }
  .contact-list .indent { padding-left: 23px; }
  .person-name {
    position: absolute; right: 30px; bottom: 26px;
    font-weight: 600; font-size: 19px;
  }
</style>
</head>
<body>
<main class="sheet">
  <section class="card card--front" aria-label="Card front">
    <div class="silver-edge"></div>
    <div class="brand-name">Marlow Reed</div>
    <ul class="contact-list">
      <li>
        <svg viewBox="0 0 16 16" aria-hidden="true"><circle cx="8" cy="8" r="7.3" fill="none" stroke="#fff" stroke-width="1.2"/><path d="M5.3 4.2c.4-.3.8-.2 1 .2l.7 1.3c.2.4 0 .7-.3.9l-.4.3c.4 1 1.2 1.8 2.2 2.3l.3-.4c.2-.3.6-.4.9-.2l1.3.7c.4.2.5.7.2 1-.6.7-1.4 1-2.3.6C7 10.2 5.5 8.7 4.8 6.6c-.3-.9 0-1.8.5-2.4z" fill="#fff"/></svg>
        <span>0198 765 432</span>
      </li>
      <li>
        <svg viewBox="0 0 16 16" aria-hidden="true"><circle cx="8" cy="8" r="7.3" fill="#fff"/><text x="8" y="11.3" text-anchor="middle" font-size="10" font-weight="700" fill="#2f4290" font-family="Arial, sans-serif">@</text></svg>
        <span>elena@marlowreedjewelry.com</span>
      </li>
      <li>
        <svg viewBox="0 0 16 16" aria-hidden="true"><circle cx="8" cy="8" r="7.3" fill="#fff"/><g fill="none" stroke="#2f4290" stroke-width="0.9"><circle cx="8" cy="8" r="5"/><ellipse cx="8" cy="8" rx="2.2" ry="5"/><line x1="3" y1="8" x2="13" y2="8"/><line x1="3.7" y1="5.5" x2="12.3" y2="5.5"/><line x1="3.7" y1="10.5" x2="12.3" y2="10.5"/></g></svg>
        <span>www.marlowreedjewelry.com</span>
      </li>
      <li>
        <svg viewBox="0 0 16 16" aria-hidden="true"><circle cx="8" cy="8" r="7.3" fill="#fff"/><path d="M8 3.4a3 3 0 0 0-3 3c0 2.2 3 5.8 3 5.8s3-3.6 3-5.8a3 3 0 0 0-3-3z" fill="#2f4290"/><circle cx="8" cy="6.4" r="1.1" fill="#fff"/></svg>
        <span>2870 Linden Avenue</span>
      </li>
      <li class="indent"><span>Bay Harbor, FL 32456</span></li>
    </ul>
    <div class="person-name">Elena Marlow Hart</div>
  </section>

  <section class="card card--back" aria-label="Card back">
    <div class="silver-edge"></div>
    <div class="brand-name">Marlow Reed</div>
  </section>
</main>
</body>
</html>
```